web site to find a reliable, local tradesman, handyman or builder for any job

Design a web site as marketplace for handyman and client.
Handyman can
* set their profile (name, address, contacts)
* search / view / apply for job offers (by setting a new offer)
Client can
* search / view job offers
* generate new job offers (title, description, max price, date, duration, location).
* select and rate a job
Main functions would be SEARCH / VIEW to see in one glance WHAT needs to be done WHERE. The contractors then exchange contacts.
Handyman

```html
<!DOCTYPE html>
<html lang="en">
<head>
<meta charset="utf-8">
<title>Handyman Marketplace – Quick Search</title>
<link rel="stylesheet" href="https://fonts.googleapis.com/css2?family=PT+Sans:wght@400;700&family=Noto+Sans:wght@400;600;700&display=swap">
<style>
:root{
  --cream:#f4efcb;
  --brown:#8a6429;
  --orange:#e8a640;
  --rust:#8b3214;
  --ink:#5b4634;
  --text:#3c3c3c;
  --white:#ffffff;
  --photo-dark:#2f2f31;
  --photo-mid:#6b6b6e;
  --photo-light:#e6e6e6;
}
*{box-sizing:border-box;margin:0;padding:0}
html,body{width:1200px;height:1087px;overflow:hidden}
body{background:var(--cream);font-family:"PT Sans",sans-serif;color:var(--text);position:relative;border:1px solid #8c8c8c;border-top:6px solid var(--brown)}
.abs{position:absolute}
a{color:inherit}
.account-tab{position:absolute;top:-6px;height:58px;width:192px;background:var(--brown);color:var(--white);font-weight:700;font-size:18px;display:flex;align-items:center;justify-content:center;border-radius:0 0 6px 6px;letter-spacing:.3px}
.main-nav{left:92px;top:111px;width:1016px;height:70px;background:var(--orange);border-radius:8px 8px 0 0;display:flex;align-items:center}
.main-nav span{font-weight:700;font-size:19px;color:var(--rust);height:44px;display:flex;align-items:center;justify-content:center;border-left:1px solid #f7d598;flex:none}
.main-nav span:first-child{border-left:none}
.main-nav .active{background:var(--rust);color:var(--white);height:70px;border:none;position:relative}
.main-nav .active::after{content:"";position:absolute;left:50%;bottom:-6px;margin-left:-4px;border:4px solid transparent;border-top:6px solid var(--white);border-bottom:none}
.sub-nav{left:76px;top:181px;width:1047px;height:42px;background:var(--rust);color:var(--white);font-size:16px;padding-left:37px;display:flex;align-items:center;gap:6px}
.panel{left:92px;top:223px;width:1016px;height:570px;background:var(--white);box-shadow:4px 4px 6px rgba(0,0,0,.15)}
.hero-photo{left:800px;top:232px;width:250px;height:262px;border-radius:10px;background:linear-gradient(180deg,var(--photo-mid) 0%,var(--photo-dark) 55%,var(--photo-light) 100%)}
.title{left:111px;top:244px;font-family:"Noto Sans",sans-serif;font-size:42px;font-weight:600;color:var(--ink)}
.field{position:absolute;background:var(--white);border:1px solid #a8a8a8;border-radius:3px;font-size:18px;color:#444;display:flex;align-items:center;padding-left:14px}
.select{padding-left:11px}
.select .arrow{position:absolute;right:-1px;top:-1px;bottom:-1px;width:38px;background:linear-gradient(#5a5a5a,#2e2e2e);border-radius:0 3px 3px 0;display:flex;align-items:center;justify-content:center}
.btn{position:absolute;color:var(--white);display:flex;align-items:center;justify-content:center;border-radius:4px}
.search-btn{left:112px;top:468px;width:138px;height:41px;background:var(--rust);font-size:22px}
.card{position:absolute;top:525px;width:308px;height:255px;background:var(--white);border:1px solid #bdbdbd;border-radius:6px;overflow:hidden}
.card-head{height:56px;display:flex;align-items:center;justify-content:center;color:var(--white);font-weight:700;font-size:22px}
.job{position:relative;height:93px;margin:0 10px;border-bottom:1px solid #ccc}
.job:last-child{border:none}
.job-logo{position:absolute;left:8px;top:6px;width:85px;height:85px;border:1px solid #aaa;display:flex;flex-direction:column;align-items:center;justify-content:center;gap:6px;font-size:13px;color:#333}
.job-logo i{display:block;width:26px;height:26px;border-radius:50%}
.job-text{position:absolute;left:121px;top:6px;width:162px;font-size:12.5px;line-height:15.3px;color:#444}
.job-text b{display:block}
.job-more{position:absolute;right:6px;bottom:4px;font-size:12px;font-weight:700;color:#555}
.cat-list{list-style:none;padding:24px 0 0 42px;font-size:17px;line-height:20.4px;color:#444}
.footer{left:76px;top:791px;width:1047px;height:241px;background:var(--rust);color:var(--white);font-size:17px}
.footer ul{list-style:none;position:absolute}
.footer li a{text-decoration:underline}
.divider{position:absolute;top:20px;height:182px;border-left:1px dashed #e8c9b8}
.social{position:absolute;top:69px;width:42px;height:42px;border-radius:5px;background:linear-gradient(#eee,#9a9a9a);border:1px solid #777;display:flex;align-items:center;justify-content:center;color:#444;font-size:9px;font-weight:700}
.bottom-links{left:762px;top:1044px;font-size:18px;color:#222}
</style>
</head>
<body>
<div class="account-tab" style="left:80px">LOGIN</div>
<div class="account-tab" style="left:284px">REGISTER</div>

<nav class="abs main-nav">
  <span style="width:97px">CLIENT</span><span class="active" style="width:131px">HANDYMAN</span><span style="width:149px;border-left:none">QUICK SEARCH</span><span style="width:182px">DETAILED SEARCH</span><span style="width:160px">CAREER TOOLS</span>
</nav>
<div class="abs sub-nav">Profile Settings &nbsp;| New Job Offers &nbsp;| &nbsp;Search Job Offers</div>

<div class="abs panel"></div>
<div class="abs hero-photo" role="img" aria-label="Photo of a happy job seeker in a dark suit sitting cross-legged with a laptop, arms raised"></div>

<h1 class="abs title">Quick Search</h1>
<div class="field" style="left:111px;top:299px;width:589px;height:46px">Keyword</div>
<div class="field select" style="left:111px;top:358px;width:270px;height:34px">All City<span class="arrow"><svg width="22" height="14"><path d="M2 2l9 9 9-9" stroke="#fff" stroke-width="3" fill="none"/></svg></span></div>
<div class="field select" style="left:429px;top:358px;width:270px;height:34px">All Position<span class="arrow"><svg width="22" height="14"><path d="M2 2l9 9 9-9" stroke="#fff" stroke-width="3" fill="none"/></svg></span></div>
<div class="field select" style="left:111px;top:417px;width:270px;height:34px">All Category<span class="arrow"><svg width="22" height="14"><path d="M2 2l9 9 9-9" stroke="#fff" stroke-width="3" fill="none"/></svg></span></div>
<div class="field select" style="left:429px;top:417px;width:270px;height:34px">All Sectors<span class="arrow"><svg width="22" height="14"><path d="M2 2l9 9 9-9" stroke="#fff" stroke-width="3" fill="none"/></svg></span></div>
<div class="btn search-btn">Search</div>

<section class="card" style="left:106px">
  <div class="card-head" style="background:var(--orange)">RECENT JOB</div>
  <div class="job">
    <div class="job-logo"><i style="background:#7cbf3a"></i>Cogwell</div>
    <div class="job-text"><b>Recent Job</b>Consectetur adipiscing elit. Nunc porttitor faucibus urna non eleifend. Morbi et justo dui.</div>
    <span class="job-more">Read more»</span>
  </div>
  <div class="job">
    <div class="job-logo"><i style="background:#d42a2a"></i>Tidy Trades</div>
    <div class="job-text"><b>Recent Job</b>Consectetur adipiscing elit. Nunc porttitor faucibus urna non eleifend. Morbi et justo dui.</div>
    <span class="job-more">Read more»</span>
  </div>
</section>

<section class="card" style="left:449px">
  <div class="card-head" style="background:var(--rust)">CAREER GUIDE</div>
  <div class="btn" style="left:30px;top:85px;width:242px;height:55px;background:var(--brown);font-size:28px">Career Test</div>
  <div class="btn" style="left:34px;top:171px;width:242px;height:55px;background:var(--orange);font-size:28px">Career Description</div>
</section>

<section class="card" style="left:786px">
  <div class="card-head" style="background:var(--brown)">JOB CATEGORY</div>
  <ul class="cat-list">
    <li>» Accounting</li><li>» Admin &amp; Clerical</li><li>» Banking &amp; Finance</li><li>» Business Opportunities</li><li>» Contract &amp; Freelance</li><li>» Customer Service</li>
  </ul>
  <div class="btn" style="left:174px;top:209px;width:119px;height:36px;background:var(--rust);font-size:21px">More</div>
</section>

<footer class="abs footer">
  <ul style="left:107px;top:52px;line-height:26.5px"><li><a>About Us</a></li><li><a>Contact Us</a></li><li><a>Job Search</a></li><li><a>Job Offers</a></li><li><a>News</a></li></ul>
  <span class="divider" style="left:256px"></span>
  <ul style="left:315px;top:48px;line-height:20.5px"><li><a>Beginner’s Guide</a></li><li><a>Latest News</a></li><li><a>All Category</a></li><li><a>Job in Your Cities</a></li></ul>
  <span class="divider" style="left:485px"></span>
  <p style="position:absolute;left:525px;top:40px;width:184px;line-height:20.3px;text-decoration:underline">Lorem Ipsum is simply<br>It is a long established<br>fact that a reader will be<br>distracted by the<br>readable content of a<br>page when looking at<br>its layout. The point of<br>using Lorem Ipsum is</p>
  <span class="divider" style="left:731px"></span>
  <span style="position:absolute;left:749px;top:53px">Follow Us:</span>
  <span class="social" style="left:831px">Friendnet</span>
  <span class="social" style="left:891px">Chirper</span>
  <span class="social" style="left:949px"><svg width="32" height="22"><rect x="1" y="1" width="30" height="20" fill="#fff" stroke="#333" stroke-width="2"/><path d="M1 1l15 11 15-11M1 21l11-10M31 21l-11-10" stroke="#333" stroke-width="2" fill="none"/></svg></span>
</footer>

<div class="abs bottom-links">Home | About Us | Contact Us | FAQ | Help</div>
</body>
</html>
```